4Star Hotel looking for web design

Hello everyone,
We are located in Cambodia, the hotel should open in 2-3 months. The name will be Velmora-Boutique Hotel. We are looking for a webdesign which is professional, elegant and SIMPLE.
All informations should be easy to find. We are quite open to proposition but we would like to the home page:
-a carousel with around 5-8 picture
-Little menu where we can book a room
By the way, we would like a page for our restaurant, gallery, contact page for description of the rooms. I add some old pictures.
I give an example of what we are expecting:
www.quenrostays.com/tovelspring
We hope that we are proposing a good job for you guys. Have fun and Thanks.
Oh and the winner ( or someone he had choose) of course have free night in our presidential suite
Target Market(s)
We are looking for european Market. Let s say people middle age who are willing to travel in difficult area
Industry/Entity Type
Hotel
Coding
Coded - Design and coding required
Number of Pages Required
5+ page
Requirements
Must have
- Simple, simple and Simple
- Carousel
- place for book a room
- during booking, a menu for select room , and after that another menu for propose like tour in town, taxi, flower, bottle of champagne for example
- during all the process, the customer should be able to know at what step it is and can stop and come back after
- Have to be perfect for smartphone
- Price with drawbar for they know how much they earn with our reduction
Nice to have
- during the process of information (name, adress, tel...), it would be great if they can fill it with a button facebook, google plus, lindkdin, instagram ....
- then a button share on facebook, twitter for know that they book in our hotel
- At the end of the booking, a flashcode with the recapitulatif that customer can scan.

```html
<!DOCTYPE html>
<html lang="en">
<head>
<meta charset="utf-8">
<title>Velmora-Boutique Hotel — Home</title>
<link rel="stylesheet" href="https://fonts.googleapis.com/css2?family=Raleway:wght@300;400;600&family=Open+Sans:wght@400;600&display=swap">
<style>
  :root{
    --teal:#2dbda3;
    --teal-dark:#229c86;
    --ink:#3b3f44;
    --muted:#9aa0a6;
    --line:#e3e6e8;
    --footer:#2c3035;
    --white:#ffffff;
    --brand:#8a2a2a;
  }
  *{box-sizing:border-box;margin:0;padding:0}
  html,body{width:870px;height:1200px;overflow:hidden;background:var(--white)}
  body{font-family:"Open Sans",Arial,sans-serif;color:var(--ink)}
  .page{position:relative;width:870px;height:1200px;overflow:hidden}

  /* hero */
  .hero{position:absolute;left:0;top:0;width:870px;height:465px;
    background:linear-gradient(180deg,#6f8fa8 0%,#9fb6c2 22%,#b4564f 48%,#8e3a36 62%,#3f6b3a 80%,#2d5630 100%)}
  .site-nav{position:absolute;left:0;top:0;width:870px;height:34px;display:flex;align-items:center;
    justify-content:space-between;padding:0 28px;background:rgba(0,0,0,.25)}
  .main-menu{display:flex;gap:22px;list-style:none}
  .main-menu li,.utility li{font-size:10px;color:var(--white);letter-spacing:.3px}
  .utility{display:flex;gap:10px;align-items:center;list-style:none}
  .social-dot{width:14px;height:14px;border-radius:50%;background:rgba(255,255,255,.85)}
  .brand-badge{position:absolute;left:362px;top:62px;width:146px;height:146px;border-radius:50%;
    background:rgba(255,255,255,.85);display:flex;flex-direction:column;align-items:center;justify-content:center;
    font-family:"Raleway",sans-serif;font-weight:600;color:var(--brand);text-align:center}
  .brand-badge .name{font-size:22px;line-height:1.1}
  .brand-badge .tag{font-size:12px;line-height:1.4}

  /* booking */
  .booking{position:absolute;left:110px;top:465px;width:650px;height:80px;background:var(--white);padding:10px 14px}
  .booking-head{display:flex;justify-content:space-between;font-size:10px;color:var(--muted)}
  .booking-head .hotel{color:var(--teal)}
  .booking-head .extra{color:var(--teal)}
  .booking-fields{display:flex;gap:8px;margin-top:10px;align-items:center}
  .field{height:26px;border:1px solid var(--line);font-size:9px;color:var(--muted);display:flex;align-items:center;
    justify-content:space-between;padding:0 8px}
  .field.date{width:92px}
  .field.select{width:88px}
  .btn-book{width:90px;height:26px;background:var(--teal);color:var(--white);font-size:9px;font-weight:600;
    display:flex;align-items:center;justify-content:center;letter-spacing:.5px;margin-left:auto}

  /* offers */
  .offers-title{position:absolute;top:568px;width:870px;text-align:center;font-family:"Raleway",sans-serif;
    font-weight:300;font-size:24px;letter-spacing:4px;color:var(--ink)}
  .offers-intro{position:absolute;top:604px;left:260px;width:350px;text-align:center;font-size:8.5px;line-height:1.5;color:var(--muted)}
  .offer-grid{position:absolute;top:648px;left:0;width:870px;height:426px;display:grid;
    grid-template-columns:repeat(4,1fr);grid-template-rows:repeat(2,1fr);gap:2px;background:var(--white)}
  .photo{width:100%;height:100%}
  .p1{background:linear-gradient(160deg,#c9b9a5,#6e4b3a)}
  .p3{background:linear-gradient(160deg,#5a3d2e,#c79b6a)}
  .p4{background:linear-gradient(160deg,#6a4d86,#d05aa0 60%,#3b2a55)}
  .p5{background:linear-gradient(160deg,#3d3b3a,#a5a2a0)}
  .p6{background:linear-gradient(160deg,#c2a77d,#5a4430)}
  .p7{background:linear-gradient(160deg,#7a8eae,#eae8e4 60%,#b23a3a)}
  .p8{background:linear-gradient(180deg,#6fa7d8,#4f7aa8 55%,#c9672f)}
  .offer-card{background:linear-gradient(160deg,rgba(45,189,163,.92),rgba(34,156,134,.95));color:var(--white);
    padding:18px 16px;position:relative}
  .offer-card .label{font-size:10px;font-weight:600;letter-spacing:.5px}
  .offer-card .price{position:absolute;right:16px;top:14px;font-family:"Raleway",sans-serif;font-size:20px;font-weight:600}
  .offer-card p{font-size:8.5px;line-height:1.5;margin-top:14px;opacity:.9}
  .offer-card .btn-details{position:absolute;left:50%;bottom:14px;transform:translateX(-50%);font-size:8.5px;
    font-weight:600;letter-spacing:1px}

  /* newsletter band */
  .newsletter{position:absolute;top:1074px;left:0;width:870px;height:82px;background:var(--teal);
    display:flex;align-items:center;padding:0 40px;color:var(--white)}
  .newsletter p{width:300px;font-size:9px;line-height:1.5}
  .btn-subscribe{margin-left:195px;width:120px;height:28px;border:1px solid rgba(255,255,255,.8);
    display:flex;align-items:center;justify-content:center;font-size:9px;letter-spacing:1px}

  /* footer */
  .site-footer{position:absolute;top:1156px;left:0;width:870px;height:44px;background:var(--footer);
    display:flex;align-items:center;justify-content:space-between;padding:0 28px;color:#c9cdd1;font-size:9px}
  .footer-links{display:flex;gap:8px;align-items:center}
  .footer-links .social-dot{background:#c9cdd1}
</style>
</head>
<body>
<div class="page">

  <header class="hero" role="img" aria-label="Hotel courtyard with red Khmer-style buildings, palm trees and garden under a blue sky">
    <nav class="site-nav">
      <ul class="main-menu">
        <li>Rooms &amp; Suites</li><li>Restaurant</li><li>Gallery</li><li>Blog</li><li>Special Offers</li>
      </ul>
      <ul class="utility">
        <li>Sign in</li><li>|</li><li>Contact</li>
        <li class="social-dot"></li><li class="social-dot"></li><li class="social-dot"></li>
      </ul>
    </nav>
    <div class="brand-badge">
      <span class="name">Velmora</span>
      <span class="tag">Boutique Hotel</span>
    </div>
  </header>

  <section class="booking">
    <div class="booking-head">
      <span>Fill the form to book room in <span class="hotel">Velmora-Boutique Hotel</span></span>
      <span class="extra">Additional Option</span>
    </div>
    <div class="booking-fields">
      <div class="field date">Check in
        <svg width="9" height="9" viewBox="0 0 9 9"><rect x=".5" y="1.5" width="8" height="7" fill="none" stroke="#9aa0a6"/><line x1=".5" y1="3.5" x2="8.5" y2="3.5" stroke="#9aa0a6"/></svg></div>
      <div class="field date">Check out
        <svg width="9" height="9" viewBox="0 0 9 9"><rect x=".5" y="1.5" width="8" height="7" fill="none" stroke="#9aa0a6"/><line x1=".5" y1="3.5" x2="8.5" y2="3.5" stroke="#9aa0a6"/></svg></div>
      <div class="field select">Adults <svg width="7" height="5" viewBox="0 0 7 5"><path d="M0 0h7L3.5 5z" fill="#9aa0a6"/></svg></div>
      <div class="field select">Children <svg width="7" height="5" viewBox="0 0 7 5"><path d="M0 0h7L3.5 5z" fill="#9aa0a6"/></svg></div>
      <div class="field select">Rooms <svg width="7" height="5" viewBox="0 0 7 5"><path d="M0 0h7L3.5 5z" fill="#9aa0a6"/></svg></div>
      <div class="btn-book">BOOK NOW</div>
    </div>
  </section>

  <h2 class="offers-title">SPECIAL OFFERS</h2>
  <p class="offers-intro">Hand-picked stays and seasonal packages for travellers who seek quiet comfort in the hills of northeast Cambodia, with rewards for early guests.</p>

  <section class="offer-grid">
    <div class="photo p1" role="img" aria-label="Twin bedroom with warm lighting"></div>
    <article class="offer-card">
      <div class="label">HOTEL SUMMER 2016</div>
      <div class="price">$150</div>
      <p>Three nights in a garden suite with breakfast and a river tour included.</p>
      <div class="btn-details">DETAILS</div>
    </article>
    <div class="photo p3" role="img" aria-label="Hotel lounge with dining table"></div>
    <div class="photo p4" role="img" aria-label="Bar area with purple and pink lighting"></div>
    <div class="photo p5" role="img" aria-label="Modern bathroom with stone finishes"></div>
    <div class="photo p6" role="img" aria-label="Spacious suite with large bed"></div>
    <div class="photo p7" role="img" aria-label="Bright bedroom with white linen"></div>
    <div class="photo p8" role="img" aria-label="Terrace with chairs overlooking sea and mountains"></div>
  </section>

  <section class="newsletter">
    <p>Join our letter for new offers, seasonal rates and events held at the hotel during the year.</p>
    <div class="btn-subscribe">SUBSCRIBE</div>
  </section>

  <footer class="site-footer">
    <span>© 2015 Velmora Boutique Hotel</span>
    <div class="footer-links">
      <span>Contact</span><span>|</span><span>Careers</span><span>|</span><span>Follow Us</span>
      <span class="social-dot"></span><span class="social-dot"></span><span class="social-dot"></span>
    </div>
  </footer>

</div>
</body>
</html>
```